Verin Court Nine Flash website

we need a website to cater to 2 aspect of the business. We have Verin court residence and verin court office. For the office, we will get their inquire and arrange a face to face meetup to show them the office area for rent. For the residence side, it will need to be like lodgly or staymira.com. we want to allow them to book online for the date they need. We have a total of 10 different room configurations starting at $70 per night and up depending on the size of the room. example of the design is https://pelvandale.com/

Target Market(s)

the website should have detail information on the layout, designs, and luxury of the building.

Industry/Entity Type

office and service appartment rental/lease

Coding

Coded - Design and coding required

Number of Pages Required

5+ page

Requirements
Must have
• a luxury perspective
Nice to have
• example https://pelvandale.com/

```html
<!DOCTYPE html>
<html lang="en">
<head>
<meta charset="utf-8">
<title>Verin Court Nine</title>
<link href="https://fonts.googleapis.com/css2?family=Cinzel:wght@400;500&family=Barlow:wght@400;500;600&display=swap" rel="stylesheet">
<style>
:root{
  --gold:#c9a02e;
  --ink:#2f2f2f;
  --text:#444;
  --muted:#8a8a8a;
  --soft:#f3f3f3;
  --white:#fff;
  --dark:#2b2b2b;
  --dark-2:#2e2e2e;
}
*{margin:0;padding:0;box-sizing:border-box}
html,body{width:1200px;height:4364px;overflow:hidden}
body{position:relative;background:var(--white);font-family:"Barlow",sans-serif;color:var(--text)}
.abs{position:absolute}
.serif{font-family:"Cinzel",serif;font-weight:400}
.btn{position:absolute;background:var(--gold);color:var(--white);font:500 12px "Barlow",sans-serif;letter-spacing:.5px;display:flex;align-items:center;justify-content:center;text-transform:uppercase}

.site-header{position:absolute;left:0;top:0;width:1200px;height:73px;background:var(--white)}
.brand{position:absolute;left:107px;top:20px;font:400 24px "Cinzel",serif;color:var(--gold);display:flex;align-items:center;gap:12px}
.brand-mark{width:26px;height:26px;border:1.5px solid var(--gold)}
.nav a{position:absolute;top:28px;font:500 12px "Barlow",sans-serif;color:var(--ink);text-decoration:none;text-transform:uppercase}
.nav .active::after{content:"";position:absolute;left:0;right:0;bottom:-10px;height:1.5px;background:var(--gold)}
.nav-cta{left:961px;top:19px;width:134px;height:37px}

.hero-photo{left:0;top:73px;width:1200px;height:602px;background:linear-gradient(90deg,#f0efed 0%,#ebe9e5 35%,#dcd8d1 60%,#9b978f 85%,#5b5853 100%)}
.hero-welcome{left:112px;top:238px;font-size:27px;color:var(--ink);display:flex;align-items:center;gap:8px}
.hero-welcome span{display:block;width:120px;height:1.5px;background:var(--ink)}
.hero-name{left:110px;top:272px;font-size:47px;color:var(--gold)}
.hero-title{left:112px;top:325px;font-size:55px;color:var(--ink);letter-spacing:1px}

.intro-frame{left:153px;top:834px;width:876px;height:247px;border:1px solid #bdbdbd}
.intro-title{left:380px;top:808px;width:420px;text-align:center;background:var(--white);font-size:44px;color:var(--gold)}
.intro-text{left:205px;top:880px;width:770px;text-align:center;font-size:16px;line-height:27px;color:var(--text)}
.outline-btn{left:510px;top:997px;width:171px;height:49px;border:1px solid #bbb;display:flex;align-items:center;justify-content:center;font:500 15px "Barlow",sans-serif;color:var(--ink);background:var(--white)}
.outline-btn::before,.outline-btn::after{content:"";position:absolute;width:24px;height:18px}
.outline-btn::before{left:-4px;top:-4px;border-left:3px solid var(--gold);border-top:3px solid var(--gold)}
.outline-btn::after{right:-4px;bottom:-4px;border-right:3px solid var(--gold);border-bottom:3px solid var(--gold)}

.stem{position:absolute;width:1px;background:#555}
.stem::after{content:"";position:absolute;left:-9px;bottom:0;width:19px;height:1px;background:#555}

.rooms-band{left:0;top:1208px;width:1200px;height:1636px;background:var(--soft)}
.section-title{position:absolute;left:0;width:1200px;text-align:center;font-size:37px;color:var(--ink);letter-spacing:1px}
.room-photo{position:absolute}
.room-notch{position:absolute;background:var(--white)}
.room-title{position:absolute;font-size:28px;color:var(--ink);white-space:nowrap}
.room-title::after{content:"";position:absolute;left:0;top:46px;width:50px;height:2px;background:var(--gold)}
.room-text{position:absolute;width:375px;font-size:16px;line-height:27px;color:var(--text)}
.room-btn{width:150px;height:33px}

.office-photo{position:absolute;top:2987px;height:271px}
.office-card{position:absolute;top:3226px;height:118px;background:#f4f4f4;text-align:center;padding-top:22px}
.office-card h3{font:400 18px "Cinzel",serif;color:var(--ink);margin-bottom:8px}
.office-card p{font-size:12.5px;line-height:17px;color:var(--muted);padding:0 36px}
.office-card.featured{background:var(--gold);height:123px;padding-top:26px}
.office-card.featured h3,.office-card.featured p{color:var(--white)}

.contact-band{left:0;top:3437px;width:1200px;height:521px;background:var(--dark)}
.contact-rule{left:0;top:3578px;width:102px;height:1px;background:#aaa}
.contact-rule::after{content:"";position:absolute;right:0;top:-7px;width:1px;height:15px;background:#aaa}
.contact-title{left:125px;top:3553px;font-size:41px;color:var(--white);letter-spacing:1px}
.contact-item{position:absolute;left:124px;display:flex;align-items:center;gap:14px;font-size:20px;color:var(--white);line-height:32px}
.contact-icon{width:36px;height:36px;border-radius:50%;background:var(--white);display:flex;align-items:center;justify-content:center;flex:none}
.field{position:absolute;border:1.5px solid #d8d8d8;font:600 14px "Barlow",sans-serif;color:var(--white);padding:16px 0 0 22px}
.send-btn{left:542px;top:3821px;width:192px;height:45px;font-size:15px}

.footer-band{left:0;top:3958px;width:1200px;height:406px;background:var(--dark-2)}
.footer-col-line{position:absolute;top:3966px;width:1px;height:322px;background:#474747}
.footer-brand{left:90px;top:4132px;width:342px;text-align:center;font-size:33px;color:var(--gold)}
.footer-head{position:absolute;top:4028px;font:400 18px "Cinzel",serif;color:var(--white);padding-left:32px}
.footer-head::before{content:"";position:absolute;left:0;top:-1px;width:3px;height:26px;background:var(--gold)}
.footer-links{position:absolute;top:4066px;list-style:none;font-size:14px;line-height:30px;color:#c8c8c8}
.socials{left:862px;top:4074px;display:flex;flex-wrap:wrap;gap:8px 14px;width:300px;font-size:13px;color:var(--white)}
.socials span{display:flex;align-items:center;gap:5px}
.socials i{width:9px;height:9px;border-radius:50%;background:var(--white);display:block}
.copy-rule{left:0;top:4288px;width:1200px;height:1px;background:#474747}
.copyright{left:0;top:4312px;width:1200px;text-align:center;font-size:12px;color:#b8b8b8}
</style>
</head>
<body>

<header class="site-header">
  <div class="brand"><span class="brand-mark"></span>Verin Court Nine</div>
  <nav class="nav">
    <a class="active" style="left:427px">About Us</a>
    <a style="left:541px">Office Space</a>
    <a style="left:678px">Blogs</a>
    <a style="left:771px">Gallery</a>
    <a style="left:875px">Why Us</a>
  </nav>
  <div class="btn nav-cta">Contact Us</div>
</header>

<section>
  <div class="abs hero-photo" role="img" aria-label="Bright luxury living room with chandelier, velvet sofa and round marble coffee table"></div>
  <div class="abs serif hero-welcome">Welcome to<span></span></div>
  <div class="abs serif hero-name">Verin Court Nine</div>
  <div class="abs serif hero-title">Residence Space</div>
  <div class="btn" style="left:120px;top:407px;width:163px;height:37px">Learn More</div>
</section>

<section>
  <div class="abs intro-frame"></div>
  <div class="abs serif intro-title">Verin Court Nine</div>
  <p class="abs intro-text">Lorem ipsum dolor sit amet, consectetur adipiscing elit, sed do eiusmod tempor incididunt ut labore et dolore magna Ut enim ad minim veniam, quis nostrud exercitation ullamco laboris nisi ut aliquip ex ea commodo consequat. Duis aute irure dolor in reprehenderit in voluptate velit</p>
  <div class="abs outline-btn">LEARN MORE</div>
</section>

<section>
  <div class="abs rooms-band"></div>
  <div class="stem" style="left:592px;top:1141px;height:96px"></div>
  <h2 class="section-title serif" style="top:1250px">Room Listings</h2>

  <div class="room-photo" style="left:571px;top:1361px;width:541px;height:403px;background:linear-gradient(180deg,#f1efeb,#e4e0da 70%,#9f9a92)" role="img" aria-label="White panelled lounge with chandelier, wall sconces and beige sofas"></div>
  <div class="room-notch" style="left:554px;top:1381px;width:43px;height:363px"></div>
  <h3 class="room-title serif" style="left:186px;top:1452px">Room Title Here</h3>
  <p class="room-text" style="left:187px;top:1507px">Lorem ipsum dolor sit amet, consectetur adipiscing elit, sed do eiusmod tempor incididunt ut labore et dolore magna Ut enim ad minim veniam, quis nostrud exercitation ullamco</p>
  <div class="btn room-btn" style="left:185px;top:1632px">Learn More</div>

  <div class="room-photo" style="left:125px;top:1834px;width:558px;height:402px;background:linear-gradient(90deg,#d9d6d1,#8a7766 40%,#e8e4de 60%,#4a4642)" role="img" aria-label="Modern living room with wood panelling, sheer curtains and dark sectional sofa"></div>
  <div class="room-notch" style="left:630px;top:1854px;width:53px;height:358px"></div>
  <h3 class="room-title serif" style="left:678px;top:1918px">Room Title Here</h3>
  <p class="room-text" style="left:678px;top:1974px">Lorem ipsum dolor sit amet, consectetur adipiscing elit, sed do eiusmod tempor incididunt ut labore et dolore magna Ut enim ad minim veniam, quis nostrud exercitation ullamco</p>
  <div class="btn room-btn" style="left:676px;top:2098px">Learn More</div>

  <div class="room-photo" style="left:564px;top:2302px;width:560px;height:408px;background:linear-gradient(90deg,#d8d2c8,#5a5b5d 45%,#3f4144 80%,#8c8178)" role="img" aria-label="Lounge with charcoal panelled walls, crystal chandelier and taupe sofa"></div>
  <div class="room-notch" style="left:564px;top:2336px;width:38px;height:351px"></div>
  <h3 class="room-title serif" style="left:193px;top:2400px">Room Title Here</h3>
  <p class="room-text" style="left:193px;top:2455px">Lorem ipsum dolor sit amet, consectetur adipiscing elit, sed do eiusmod tempor incididunt ut labore et dolore magna Ut enim ad minim veniam, quis nostrud exercitation ullamco</p>
  <div class="btn room-btn" style="left:192px;top:2580px">Learn More</div>

  <div class="stem" style="left:600px;top:2771px;height:94px"></div>
</section>

<section>
  <h2 class="section-title serif" style="top:2897px">Office Space Listings</h2>
  <div class="office-photo" style="left:66px;width:349px;background:linear-gradient(135deg,#d6d6d4,#efefee 55%,#8e8e8c)" role="img" aria-label="Reception lobby with marble wall and white curved desk"></div>
  <div class="office-photo" style="left:420px;width:351px;background:linear-gradient(180deg,#f3f3f2,#dcdcdb 55%,#3a3a3a)" role="img" aria-label="Meeting room with white table and black office chairs"></div>
  <div class="office-photo" style="left:776px;width:349px;background:linear-gradient(135deg,#5c5a57,#c9c4bd 45%,#d27a2c 70%,#9cc23f)" role="img" aria-label="Lounge area with orange and green designer chairs and pendant lamps"></div>

  <div class="office-card" style="left:86px;width:319px"><h3>Office Space Title</h3><p>Lorem ipsum dolor sit amet, consectetur adipiscing elit sed do eiusmod</p></div>
  <div class="office-card featured" style="left:436px;width:318px"><h3>Office Space Title</h3><p>Lorem ipsum dolor sit amet, consectetur adipiscing elit sed do eiusmod</p></div>
  <div class="office-card" style="left:792px;width:318px;top:3228px"><h3>Office Space Title</h3><p>Lorem ipsum dolor sit amet, consectetur adipiscing elit sed do eiusmod</p></div>
</section>

<section>
  <div class="abs contact-band"></div>
  <div class="abs contact-rule"></div>
  <h2 class="abs serif contact-title">Contact Us</h2>

  <div class="contact-item" style="top:3638px">
    <span class="contact-icon"><svg width="18" height="18" viewBox="0 0 24 24"><path fill="#2b2b2b" d="M6.6 10.8a15 15 0 0 0 6.6 6.6l2.2-2.2c.3-.3.7-.4 1-.2 1.1.4 2.300.6 3.600.6.6 0 1 .4 1 1V20c0 .6-.4 1-1 1A17 17 0 0 1 3 4c0-.6.4-1 1-1h3.5c.6 0 1 .4 1 1 0 1.3.2 2.5.6 3.6.1.3 0 .7-.2 1z"/></svg></span>
    (+100) 555 0148
  </div>
  <div class="contact-item" style="top:3703px">
    <span class="contact-icon"><svg width="18" height="18" viewBox="0 0 24 24"><rect x="3" y="6" width="18" height="12" rx="1" fill="#2b2b2b"/><path d="M3.5 7l8.5 6 8.5-6" fill="none" stroke="#fff" stroke-width="1.5"/></svg></span>
    enquiry@verincourtnine.com
  </div>
  <div class="contact-item" style="top:3764px;align-items:flex-start">
    <span class="contact-icon" style="margin-top:-2px"><svg width="18" height="18" viewBox="0 0 24 24"><path fill="#2b2b2b" d="M12 2a7 7 0 0 0-7 7c0 5 7 13 7 13s7-8 7-13a7 7 0 0 0-7-7zm0 9.5A2.5 2.5 0 1 1 12 6.5a2.5 2.5 0 0 1 0 5z"/></svg></span>
    <span>48 Lantern Row<br>Riverside City, Calmera</span>
  </div>

  <form>
    <div class="field" style="left:541px;top:3566px;width:240px;height:50px">First Name</div>
    <div class="field" style="left:790px;top:3566px;width:241px;height:50px">Last Name</div>
    <div class="field" style="left:541px;top:3627px;width:240px;height:49px">Phone</div>
    <div class="field" style="left:790px;top:3627px;width:241px;height:49px">Email</div>
    <div class="field" style="left:541px;top:3688px;width:493px;height:114px">Leave Message</div>
    <div class="btn send-btn">Send Message</div>
  </form>
</section>

<footer>
  <div class="abs footer-band"></div>
  <div class="footer-col-line" style="left:453px"></div>
  <div class="footer-col-line" style="left:646px"></div>
  <div class="footer-col-line" style="left:832px"></div>
  <div class="abs serif footer-brand">Verin Court Nine</div>

  <div class="footer-head" style="left:454px">Navigation</div>
  <ul class="footer-links" style="left:486px"><li>Home</li><li>About</li><li>Ofice Space</li><li>Testimonials</li></ul>

  <div class="footer-head" style="left:640px">Resources</div>
  <ul class="footer-links" style="left:672px"><li>Privacy Policy</li><li>Terms of Use</li><li>FAQ</li><li>Contact Us</li></ul>

  <div class="footer-head" style="left:834px;padding-left:20px">Stay in Touch</div>
  <div class="abs socials"><span><i></i>Frendly</span><span><i></i>Chirp</span><span><i></i>Linkora</span><span><i></i>Vidreel</span><span><i></i>Snapgram</span></div>

  <div class="abs copy-rule"></div>
  <div class="abs copyright">© 2024 Verin Court Nine. All Right Reserved</div>
</footer>

</body>
</html>
```